World Wide News and Current Affairs website

We intends to start up a new website which deals on New and Current Affairs.
Attention Designers,
We want a home page design for this project. Our business is based in the United States. Our goal is to become a well known brand.
The website would consist of a category for News, Business and Tech.
The theme should be beautiful and attention seeking. The website would take bulk of it's news from the US, and Europe.
Designers can get inspiration from already existing new websites such as ZPW, VJL, HALDRIM.
All designs should be clean and easy to navigate.

```html
<!DOCTYPE html>
<html lang="en">
<head>
<meta charset="utf-8">
<title>Dalvero – World News and Current Affairs</title>
<link href="https://fonts.googleapis.com/css2?family=Arimo:wght@400;700&family=Lato:wght@400;700;900&display=swap" rel="stylesheet">
<style>
:root{
  --red:#e0141c;
  --red-deep:#c10d12;
  --ink:#111111;
  --black:#0d0d0d;
  --paper:#ffffff;
  --stone:#e6e6e1;
  --footer:#2b2b2b;
  --muted:#8a8a8a;
  --line:#d6d6d6;
}
*{box-sizing:border-box;margin:0;padding:0}
html,body{width:1200px;height:2671px;overflow:hidden}
body{position:relative;background:var(--paper);font-family:"Lato",Arial,sans-serif;color:var(--ink)}
a{color:inherit;text-decoration:none}
.section{position:absolute;left:0;width:1200px}
.abs{position:absolute}

/* header */
.site-header{top:0;height:125px;background:var(--paper);box-shadow:0 3px 4px rgba(0,0,0,.35)}
.brand{left:78px;top:40px;display:flex;align-items:center;gap:12px;font-family:"Lato",Arial,sans-serif;font-weight:700;font-size:40px;color:var(--ink);line-height:1}
.brand-dot{width:22px;height:22px;background:var(--red)}
.search{display:flex;height:30px}
.search input{width:214px;border:1px solid #9a9a9a;border-right:none;padding:0 10px;font-family:"Lato",sans-serif;font-size:14px;color:#555;background:#fff}
.search button{width:36px;background:var(--red);border:none;display:flex;align-items:center;justify-content:center}
.header-search{left:874px;top:11px}
.main-nav{left:308px;top:70px;display:flex;font-family:"Arimo",Arial,sans-serif;font-size:19px;color:#222}
.main-nav a{margin-right:40px;padding-bottom:18px;display:flex;align-items:center;gap:6px}
.main-nav a.active{color:var(--red);border-bottom:3px solid var(--red)}

/* trending */
.trending{top:128px;height:68px;border-bottom:1px solid var(--line)}
.trend-label{left:78px;top:18px;width:137px;height:32px;background:var(--red);color:#fff;font-family:"Arimo",sans-serif;font-weight:700;font-size:14px;display:flex;align-items:center;justify-content:center;gap:8px}
.trend-text{left:242px;top:24px;font-size:16px;color:#333}
.pager{display:flex;gap:12px}
.pager svg{width:31px;height:31px}
.trend-pager{left:1048px;top:19px}

/* hero */
.hero{top:198px;height:470px}
.hero-tile{position:absolute;overflow:hidden}
.hero-tile .photo{position:absolute;inset:0}
.hero-tile .shade{position:absolute;inset:0;background:linear-gradient(to bottom,rgba(0,0,0,0) 40%,rgba(0,0,0,.55))}
.tag{position:absolute;background:var(--red);color:#fff;font-family:"Arimo",sans-serif;font-weight:700;font-size:15px;display:flex;align-items:center;justify-content:center}
.dateline{position:absolute;color:#fff;font-size:15px;display:flex;align-items:center;gap:8px}
.hero-title{position:absolute;color:#fff;font-weight:700}

/* latest */
.latest{top:675px;height:522px;background:var(--black);color:#fff}
.section-title{position:absolute;font-family:"Arimo",Arial,sans-serif;font-size:37px;font-weight:400}
.latest .section-title{left:78px;top:40px}
.latest-pager{left:1048px;top:60px}
.latest-card{position:absolute;top:115px;width:333px}
.latest-card .photo{height:218px;position:relative}
.date-flag{position:absolute;left:0;top:0;width:64px;height:80px;clip-path:polygon(0 0,100% 0,100% 100%,50% 80%,0 100%);text-align:center;font-family:"Arimo",sans-serif;padding-top:4px}
.date-flag b{display:block;font-size:30px;font-weight:400;line-height:1.05}
.date-flag span{font-size:13px}
.flag-white{background:#fff;color:#111}
.flag-red{background:var(--red);color:#fff}
.latest-card h3{margin-top:28px;color:var(--red);font-weight:400;font-size:17px}
.latest-card p{margin-top:10px;font-size:16px;line-height:25px;width:310px}
.read-more{display:flex;align-items:center;gap:8px;margin-top:12px;color:var(--red);font-size:15px}

/* categories */
.categories{top:1197px;height:574px;background:var(--stone)}
.cat-col{position:absolute;top:0;width:330px}
.cat-col h2{position:absolute;top:52px;font-family:"Arimo",Arial,sans-serif;font-weight:400;font-size:37px}
.cat-item{position:absolute;left:0;width:330px;height:103px}
.cat-item .photo{position:absolute;left:0;top:0;width:155px;height:103px}
.cat-item .info{position:absolute;left:168px;top:0}
.cat-item h4{color:var(--red);font-weight:400;font-size:16px}
.cat-item .meta{margin-top:7px;font-size:14px;color:var(--muted);display:flex;align-items:center;gap:7px}
.cat-item p{margin-top:9px;font-size:15px;line-height:25px;color:var(--muted);width:168px}
.view-all{position:absolute;top:506px;color:var(--red);font-size:15px;display:flex;align-items:center;gap:8px}

/* editor's picks */
.picks{top:1771px;height:397px;background:#fff}
.picks .section-title{left:90px;top:38px}
.picks-bar{left:76px;top:45px;width:5px;height:32px;background:var(--red)}
.picks-pager{left:1048px;top:44px}
.pick{position:absolute;top:125px;width:241px;height:208px}
.pick-feature{background:var(--red-deep);color:#fff;padding:18px 0 0 33px}
.pick-feature h3{font-size:23px;font-weight:700}
.pick-feature .meta{margin-top:6px;font-size:14px;display:flex;align-items:center;gap:7px}
.pick-feature p{margin-top:7px;font-size:15px;line-height:23px;width:175px}

/* weather strip */
.weather{top:2168px;height:84px;background:var(--black);color:#fff}
.weather-place{left:80px;top:29px;font-size:17px;display:flex;align-items:center;gap:22px}
.footer-search{left:874px;top:27px}
.footer-search input{background:#000;color:#ddd;border-color:#bbb}

/* footer links */
.footer{top:2252px;height:324px;background:var(--footer);color:#fff}
.footer-col{position:absolute;top:34px}
.footer-col h5{font-family:"Arimo",sans-serif;font-weight:400;font-size:20px}
.footer-col ul{list-style:none;margin-top:18px}
.footer-col li{font-size:15px;height:33.5px;display:flex;align-items:center;gap:10px}
.footer-col li svg{color:var(--red)}

/* legal */
.legal{top:2576px;height:95px;background:var(--red-deep);color:#fff;text-align:center}
.legal-links{margin-top:12px;font-size:15px;display:flex;justify-content:center}
.legal-links a{padding:0 10px;border-left:1px solid #fff}
.legal-links a:first-child{border-left:none}
.copyright{margin-top:16px;font-size:15px}
</style>
</head>
<body>

<svg width="0" height="0" style="position:absolute">
  <defs>
    <symbol id="cal" viewBox="0 0 12 12"><rect x="1" y="2" width="10" height="9" fill="none" stroke="currentColor" stroke-width="1.4"/><rect x="1" y="2" width="10" height="3" fill="currentColor"/><rect x="3" y="0.5" width="1.5" height="2.5" fill="currentColor"/><rect x="7.5" y="0.5" width="1.5" height="2.5" fill="currentColor"/></symbol>
    <symbol id="chev2" viewBox="0 0 12 10"><path d="M1 1l4 4-4 4M6 1l4 4-4 4" fill="none" stroke="currentColor" stroke-width="1.8"/></symbol>
    <symbol id="prev-grey" viewBox="0 0 32 32"><circle cx="16" cy="16" r="14.5" fill="none" stroke="#888" stroke-width="2"/><path d="M18 10l-6 6 6 6" fill="none" stroke="#888" stroke-width="2.4"/></symbol>
    <symbol id="next-red" viewBox="0 0 32 32"><circle cx="16" cy="16" r="14.5" fill="none" stroke="#e0141c" stroke-width="2"/><path d="M14 10l6 6-6 6" fill="none" stroke="#e0141c" stroke-width="2.4"/></symbol>
    <symbol id="prev-white" viewBox="0 0 32 32"><circle cx="16" cy="16" r="14.5" fill="none" stroke="#ddd" stroke-width="1.6"/><path d="M18 10l-6 6 6 6" fill="none" stroke="#ddd" stroke-width="2"/></symbol>
    <symbol id="next-white" viewBox="0 0 32 32"><circle cx="16" cy="16" r="14.5" fill="none" stroke="#ddd" stroke-width="1.6"/><path d="M14 10l6 6-6 6" fill="none" stroke="#ddd" stroke-width="2"/></symbol>
    <symbol id="prev-red" viewBox="0 0 32 32"><circle cx="16" cy="16" r="14.5" fill="none" stroke="#e0141c" stroke-width="1.6"/><path d="M18 10l-6 6 6 6" fill="none" stroke="#e0141c" stroke-width="2"/></symbol>
    <symbol id="next-grey" viewBox="0 0 32 32"><circle cx="16" cy="16" r="14.5" fill="none" stroke="#555" stroke-width="1.6"/><path d="M14 10l6 6-6 6" fill="none" stroke="#555" stroke-width="2"/></symbol>
    <symbol id="glass" viewBox="0 0 14 14"><circle cx="5.8" cy="5.8" r="4.2" fill="none" stroke="#fff" stroke-width="2"/><path d="M9 9l4 4" stroke="#fff" stroke-width="2.2"/></symbol>
  </defs>
</svg>

<header class="section site-header">
  <a class="abs brand" href="#"><span class="brand-dot"></span>Dalvero</a>
  <form class="abs search header-search"><input type="text" value="Search Dalvero..."><button type="button"><svg width="15" height="15"><use href="#glass"/></svg></button></form>
  <nav class="abs main-nav">
    <a class="active" href="#">HOME</a>
    <a href="#">ABOUT US</a>
    <a href="#">NEWS</a>
    <a href="#">BUSINESS</a>
    <a href="#">TECHNOLOGY</a>
    <a href="#">VIDEO</a>
    <a href="#">MORE <svg width="10" height="7" viewBox="0 0 10 7"><path d="M0 0h10L5 6z" fill="#222"/></svg></a>
  </nav>
</header>

<section class="section trending">
  <div class="abs trend-label"><svg width="8" height="14" viewBox="0 0 8 14"><path d="M5 0L0 8h3l-1 6 6-9H5z" fill="#fff"/></svg>TRENDING</div>
  <p class="abs trend-text">News Title : Lorem Ipsum is simply dummy text of the printing and typesetting industry.</p>
  <div class="abs pager trend-pager"><svg><use href="#prev-grey"/></svg><svg><use href="#next-red"/></svg></div>
</section>

<section class="section hero">
  <article class="hero-tile" style="left:0;top:0;width:596px;height:470px">
    <div class="photo" role="img" aria-label="Two heads of state speaking at podiums in a formal hall" style="background:linear-gradient(135deg,#6d5a45 0%,#3a3530 45%,#8a7a60 70%,#2b2c33 100%)"></div>
    <div class="shade"></div>
    <span class="tag" style="left:43px;top:316px;width:82px;height:27px">News</span>
    <span class="dateline" style="left:43px;top:363px"><svg width="13" height="13"><use href="#cal"/></svg>April 21st, 2017</span>
    <h2 class="hero-title" style="left:45px;top:390px;font-size:33px">News Title</h2>
  </article>
  <article class="hero-tile" style="left:605px;top:0;width:595px;height:229px">
    <div class="photo" role="img" aria-label="Person working on a laptop above a night city skyline" style="background:linear-gradient(120deg,#1d2535 0%,#3a3f55 40%,#4a3a3e 70%,#1a1a22 100%)"></div>
    <div class="shade"></div>
    <span class="tag" style="left:42px;top:92px;width:84px;height:26px">News</span>
    <span class="dateline" style="left:42px;top:137px"><svg width="13" height="13"><use href="#cal"/></svg>April 21st, 2017</span>
    <h2 class="hero-title" style="left:45px;top:166px;font-size:31px">News Title</h2>
  </article>
  <article class="hero-tile" style="left:605px;top:240px;width:595px;height:230px">
    <div class="photo" role="img" aria-label="Reporters holding microphones toward a speaker" style="background:linear-gradient(110deg,#4a4a55 0%,#8a7c80 35%,#a0303a 60%,#2f2f35 100%)"></div>
    <div class="shade"></div>
    <span class="tag" style="left:42px;top:89px;width:84px;height:26px">News</span>
    <span class="dateline" style="left:42px;top:134px"><svg width="13" height="13"><use href="#cal"/></svg>April 21st, 2017</span>
    <h2 class="hero-title" style="left:45px;top:163px;font-size:31px">News Title</h2>
  </article>
</section>

<section class="section latest">
  <h2 class="section-title">All The Latest News</h2>
  <div class="abs pager latest-pager"><svg><use href="#prev-white"/></svg><svg><use href="#next-white"/></svg></div>
  <article class="latest-card" style="left:78px">
    <div class="photo" role="img" aria-label="Family gathered around an interactive display table in a museum" style="background:linear-gradient(135deg,#2a211c,#6b4a32 50%,#a47a4e 80%,#3a2c22)"><div class="date-flag flag-white"><b>22</b><span>APRIL</span></div></div>
    <h3>Lorem Ipsum is simply text Dummy</h3>
    <p>Lorem Ipsum is simply dummy text of the printing and typesetting industry.</p>
    <a class="read-more" href="#">READ MORE <svg width="12" height="10"><use href="#chev2"/></svg></a>
  </article>
  <article class="latest-card" style="left:434px">
    <div class="photo" role="img" aria-label="Hand touching a glowing cybersecurity tablet interface" style="background:linear-gradient(135deg,#c8d4e0,#5a86b0 45%,#2a4a80 70%,#9ab0c6)"><div class="date-flag flag-red"><b>22</b><span>APRIL</span></div></div>
    <h3>Lorem Ipsum is simply text Dummy</h3>
    <p>Lorem Ipsum is simply dummy text of the printing and typesetting industry.</p>
    <a class="read-more" href="#">READ MORE <svg width="12" height="10"><use href="#chev2"/></svg></a>
  </article>
  <article class="latest-card" style="left:790px">
    <div class="photo" role="img" aria-label="Businessman in a suit standing before a digital city backdrop" style="background:linear-gradient(135deg,#9a9a9a,#d0d0d0 40%,#5a5a5a 70%,#b8b8b8)"><div class="date-flag flag-red"><b>22</b><span>APRIL</span></div></div>
    <h3>Lorem Ipsum is simply text Dummy</h3>
    <p>Lorem Ipsum is simply dummy text of the printing and typesetting industry</p>
    <a class="read-more" href="#">READ MORE <svg width="12" height="10"><use href="#chev2"/></svg></a>
  </article>
</section>

<section class="section categories">
  <div class="cat-col" style="left:78px">
    <h2>News</h2>
    <article class="cat-item" style="top:128px"><div class="photo" role="img" aria-label="Sun over a ship at sea" style="background:linear-gradient(135deg,#9ab8d0,#4a6a8a 60%,#1c2a3a)"></div><div class="info"><h4>News Title</h4><div class="meta"><svg width="12" height="12"><use href="#cal"/></svg>April 22nd, 2017</div><p>Lorem Ipsum is simply dummy text of the...</p></div></article>
    <article class="cat-item" style="top:258px"><div class="photo" role="img" aria-label="National flag beside a stock market board" style="background:linear-gradient(135deg,#b02030,#e8e8f0 40%,#3a4a8a 70%,#2a2a50)"></div><div class="info"><h4>News Title</h4><div class="meta"><svg width="12" height="12"><use href="#cal"/></svg>April 22nd, 2017</div><p>Lorem Ipsum is simply dummy text of the...</p></div></article>
    <article class="cat-item" style="top:388px"><div class="photo" role="img" aria-label="Wall of news broadcast screens" style="background:linear-gradient(135deg,#3a3540,#6a6070 50%,#2a2530)"></div><div class="info"><h4>News Title</h4><div class="meta"><svg width="12" height="12"><use href="#cal"/></svg>April 22nd, 2017</div><p>Lorem Ipsum is simply dummy text of the...</p></div></article>
    <a class="view-all" href="#">VIEW ALL <svg width="12" height="10"><use href="#chev2"/></svg></a>
  </div>
  <div class="cat-col" style="left:438px">
    <h2>Business</h2>
    <article class="cat-item" style="top:128px"><div class="photo" role="img" aria-label="Man flying a drone at sunset" style="background:linear-gradient(135deg,#d8c8c0,#b89080 50%,#6a8070)"></div><div class="info"><h4>News Title</h4><div class="meta"><svg width="12" height="12"><use href="#cal"/></svg>April 22nd, 2017</div><p>Lorem Ipsum is simply dummy text of the...</p></div></article>
    <article class="cat-item" style="top:258px"><div class="photo" role="img" aria-label="Glowing golden coin in the dark" style="background:radial-gradient(circle at 50% 55%,#ffd070,#d07010 40%,#201008 80%)"></div><div class="info"><h4>News Title</h4><div class="meta"><svg width="12" height="12"><use href="#cal"/></svg>April 22nd, 2017</div><p>Lorem Ipsum is simply dummy text of the...</p></div></article>
    <article class="cat-item" style="top:388px"><div class="photo" role="img" aria-label="Business team in an office" style="background:linear-gradient(135deg,#eeeeee,#b8b8c0 50%,#40404a)"></div><div class="info"><h4>News Title</h4><div class="meta"><svg width="12" height="12"><use href="#cal"/></svg>April 22nd, 2017</div><p>Lorem Ipsum is simply dummy text of the...</p></div></article>
    <a class="view-all" href="#">VIEW ALL <svg width="12" height="10"><use href="#chev2"/></svg></a>
  </div>
  <div class="cat-col" style="left:794px">
    <h2>Technology</h2>
    <article class="cat-item" style="top:128px"><div class="photo" role="img" aria-label="Flag waving against a blue sky" style="background:linear-gradient(135deg,#3a70c8,#c03040 50%,#e8e8ee 65%,#4a80d0)"></div><div class="info"><h4>News Title</h4><div class="meta"><svg width="12" height="12"><use href="#cal"/></svg>April 22nd, 2017</div><p>Lorem Ipsum is simply dummy text of the...</p></div></article>
    <article class="cat-item" style="top:258px"><div class="photo" role="img" aria-label="Dark trading screens with market data" style="background:linear-gradient(135deg,#101828,#2a3050 50%,#501820)"></div><div class="info"><h4>News Title</h4><div class="meta"><svg width="12" height="12"><use href="#cal"/></svg>April 22nd, 2017</div><p>Lorem Ipsum is simply dummy text of the...</p></div></article>
    <article class="cat-item" style="top:388px"><div class="photo" role="img" aria-label="Official seated at a desk holding a signed document" style="background:linear-gradient(135deg,#2a2a30,#8a4a40 45%,#202028)"></div><div class="info"><h4>News Title</h4><div class="meta"><svg width="12" height="12"><use href="#cal"/></svg>April 22nd, 2017</div><p>Lorem Ipsum is simply dummy text of the...</p></div></article>
    <a class="view-all" href="#">VIEW ALL <svg width="12" height="10"><use href="#chev2"/></svg></a>
  </div>
</section>

<section class="section picks">
  <span class="abs picks-bar"></span>
  <h2 class="section-title">Editor's Picks</h2>
  <div class="abs pager picks-pager"><svg><use href="#prev-red"/></svg><svg><use href="#next-grey"/></svg></div>
  <article class="pick pick-feature" style="left:78px">
    <h3>News Title</h3>
    <div class="meta"><svg width="12" height="12"><use href="#cal"/></svg>April 21st, 2017</div>
    <p>Lorem Ipsum is simply dummy text of the printing and type.</p>
  </article>
  <div class="pick" style="left:345px;background:linear-gradient(135deg,#2a211c,#6b4a32 50%,#a47a4e 80%,#3a2c22)" role="img" aria-label="Family at an interactive museum display"></div>
  <div class="pick" style="left:614px;background:linear-gradient(135deg,#2a2530,#6a6575 50%,#1c1a22)" role="img" aria-label="Mosaic wall of many video screens"></div>
  <div class="pick" style="left:881px;background:radial-gradient(circle at 50% 55%,#ffd070,#d07010 40%,#201008 85%)" role="img" aria-label="Glowing swirl of golden light"></div>
</section>

<section class="section weather">
  <div class="abs weather-place">London, United Kingdom
    <svg width="42" height="26" viewBox="0 0 42 26"><circle cx="27" cy="9" r="6" fill="#fff"/><path d="M8 24a7 7 0 0 1 1-14 9 9 0 0 1 17 2 6 6 0 0 1 0 12z" fill="#fff"/></svg>
    <span style="margin-left:-8px">10°</span></div>
  <form class="abs search footer-search"><input type="text" value="Search Dalvero..."><button type="button"><svg width="15" height="15"><use href="#glass"/></svg></button></form>
</section>

<footer class="section footer">
  <div class="footer-col" style="left:80px"><h5>Useful Links</h5><ul>
    <li><svg width="10" height="9"><use href="#chev2"/></svg>Home</li>
    <li><svg width="10" height="9"><use href="#chev2"/></svg>About Us</li>
    <li><svg width="10" height="9"><use href="#chev2"/></svg>News</li>
    <li><svg width="10" height="9"><use href="#chev2"/></svg>Business</li>
    <li><svg width="10" height="9"><use href="#chev2"/></svg>Technology</li>
    <li><svg width="10" height="9"><use href="#chev2"/></svg>Video</li>
    <li><svg width="10" height="9"><use href="#chev2"/></svg>Contact Us</li></ul></div>
  <div class="footer-col" style="left:351px"><h5>Top Stories</h5><ul>
    <li><svg width="10" height="9"><use href="#chev2"/></svg>Title</li><li><svg width="10" height="9"><use href="#chev2"/></svg>Title</li><li><svg width="10" height="9"><use href="#chev2"/></svg>Title</li><li><svg width="10" height="9"><use href="#chev2"/></svg>Title</li><li><svg width="10" height="9"><use href="#chev2"/></svg>Title</li><li><svg width="10" height="9"><use href="#chev2"/></svg>Title</li><li><svg width="10" height="9"><use href="#chev2"/></svg>Title</li></ul></div>
  <div class="footer-col" style="left:621px"><h5>Video</h5><ul>
    <li><svg width="10" height="9"><use href="#chev2"/></svg>Title</li><li><svg width="10" height="9"><use href="#chev2"/></svg>Title</li><li><svg width="10" height="9"><use href="#chev2"/></svg>Title</li><li><svg width="10" height="9"><use href="#chev2"/></svg>Title</li><li><svg width="10" height="9"><use href="#chev2"/></svg>Title</li><li><svg width="10" height="9"><use href="#chev2"/></svg>Title</li><li><svg width="10" height="9"><use href="#chev2"/></svg>Title</li></ul></div>
  <div class="footer-col" style="left:892px"><h5>More...</h5><ul>
    <li><svg width="10" height="9"><use href="#chev2"/></svg>Title</li><li><svg width="10" height="9"><use href="#chev2"/></svg>Title</li><li><svg width="10" height="9"><use href="#chev2"/></svg>Title</li><li><svg width="10" height="9"><use href="#chev2"/></svg>Title</li><li><svg width="10" height="9"><use href="#chev2"/></svg>Title</li><li><svg width="10" height="9"><use href="#chev2"/></svg>Title</li><li><svg width="10" height="9"><use href="#chev2"/></svg>Title</li></ul></div>
</footer>

<section class="section legal">
  <nav class="legal-links"><a href="#">Site Feedback</a><a href="#">Corrections</a><a href="#">Advertising Guidelines</a><a href="#">Terms of Use</a><a href="#">Privacy Policy</a></nav>
  <p class="copyright">© <b>Dalvero</b> - 2017. All Rights Reserved.</p>
</section>

</body>
</html>
```